Pellmar Drones webdesign: Innovative Drones service company in agriculture

We need a new website according the following conditions:
• Main colour orange and current logo;
• Transparent – open – trustworthy – dynamic - personal;
• Use the smartness and overview characteristics of the crow (Pellmar is Latin for crow);
• Accessible to multiple target groups and markets:
o So not too horticultural, too green;
• Use contradictions:
o Future versus nostalgia;
o Smartness crow versus precision hummingbird;
o Technology versus mechanical;
• Tovari 2.4 RLX as a style icon?
• Long pager website
Updates

Website menu o Home o Crop monitoring  Applications Growth | Stress | Development | Diseases  Markets Breeding | Young plant | Potplants | Cutflowers | Vegetables | Soft fruit  Customer cases o Technology Aerial data collection | Artificial intelligence | Free data sets o About Vision | Company | Partners | Team | Career o Contact o News&downloads Logo: www.pellmardrones-example.com

Target Market(s)

agriculture: owners, crop managers
oil&gas: maintenance, quality control managers and purchase managers
logistics: ware house managers, purchase managers

Industry/Entity Type

Agribusiness

Number of Pages Required

2 page

Colors
f78f20

Requirements
Must have
• long pager website
downloads
LinkedIn
Should not have
• Not too 'green' because first impression of designers of agriculture/horticulture is using the green colour. But that is not necessary.

Keep in mind that the current logo will be updates: the circle will be more 'general' and less 'agri'. Also the green colors in the logo will be slightly darker to make it more powerful.

```html
<!DOCTYPE html>
<html lang="en">
<head>
<meta charset="utf-8">
<title>Pellmar Drones</title>
<link href="https://fonts.googleapis.com/css2?family=Rajdhani:wght@400;500;600;700&family=Raleway:wght@400;500;600;700&display=swap" rel="stylesheet">
<style>
:root{
  --orange:#f78f20;
  --green-dark:#1b3009;
  --green:#2f6b12;
  --ink:#1e1e1e;
  --text:#777;
  --light:#f4f4f4;
  --paler:#f8f8f8;
  --white:#fff;
}
*{box-sizing:border-box;margin:0;padding:0}
html,body{width:1200px;height:4525px;overflow:hidden}
body{position:relative;font-family:"Raleway",sans-serif;color:var(--ink);background:var(--white)}
.abs{position:absolute}
.head-font{font-family:"Rajdhani",sans-serif}
section,header,footer{position:absolute;left:0;width:1200px}
.btn{position:absolute;background:var(--orange);color:#fff;font:700 11px "Raleway",sans-serif;letter-spacing:.3px;display:flex;align-items:center;justify-content:center;text-transform:uppercase}
.photo{position:absolute}
.title{position:absolute;left:0;width:1200px;text-align:center;font:700 38px "Rajdhani",sans-serif;letter-spacing:.5px}
.body-text{font-size:12.5px;line-height:19.5px;color:var(--text)}

/* header */
.site-header{top:0;height:74px;background:#fff}
.logo{left:93px;top:20px;display:flex;align-items:center;gap:10px}
.logo-mark{width:34px;height:34px;border-radius:50%;background:var(--orange)}
.logo-name{font:700 24px "Rajdhani",sans-serif;color:var(--orange);letter-spacing:.5px}
.topbar{left:800px;top:0;width:400px;height:30px;background:var(--orange);color:#fff;font-size:11px;display:flex;align-items:center;gap:20px;padding-left:8px}
.topbar span{display:flex;align-items:center;gap:5px}
.nav a{position:absolute;top:47px;font-size:11px;color:#333;text-decoration:none;font-weight:500}
.nav a.active{color:var(--orange)}

/* hero */
.hero{top:74px;height:525px;overflow:hidden}
.hero-photo{left:0;top:0;width:1200px;height:525px;background:linear-gradient(160deg,#d9dcd4 0%,#6d8f3a 30%,#3e6d23 55%,#8c3a2a 80%,#4d6b2c 100%)}
.hero-copy{left:669px;top:196px;color:#fff}
.hero-copy .kicker{font:500 30px "Rajdhani",sans-serif;letter-spacing:.5px}
.hero-copy h1{font:700 46px/50px "Rajdhani",sans-serif;letter-spacing:.8px}

/* welcome */
.welcome{top:599px;height:552px}
.welcome .kicker{left:93px;top:148px;font-size:15px;font-weight:500}
.welcome h2{position:absolute;left:93px;top:166px;font:700 36px "Rajdhani",sans-serif;letter-spacing:.5px}
.welcome p{left:93px;top:222px;width:510px;position:absolute}
.welcome-photo{left:666px;top:28px;width:441px;height:461px;background:linear-gradient(180deg,#fff 0%,#c9d6d8 25%,#5f7a45 45%,#2f4a34 70%,#4e6a33 100%)}

/* applications */
.applications{top:1151px;height:293px;background:var(--light)}
.applications .kicker{position:absolute;top:42px;width:1200px;text-align:center;font-size:15px;font-weight:500}
.app{position:absolute;top:128px;width:200px;text-align:center}
.app-icon{width:92px;height:92px;margin:0 auto;border-radius:50%;background:var(--orange);border:5px solid var(--green-dark);display:flex;align-items:center;justify-content:center}
.app-label{margin-top:14px;font:700 22px "Rajdhani",sans-serif;letter-spacing:.5px}

/* technology + team */
.tech{top:1444px;height:954px;background:var(--paler)}
.card{position:absolute;width:325px}
.card .photo{position:relative;height:197px;width:325px}
.card h3{font:500 17px "Raleway",sans-serif;margin-top:17px;color:#222}
.card p{margin-top:8px}
.member{position:absolute;top:578px;width:239px;text-align:center}
.member .photo{position:relative;height:264px;width:239px}
.member h4{font:600 16px "Rajdhani",sans-serif;margin-top:17px;letter-spacing:.5px}
.member span{display:block;font-size:10px;margin-top:3px}
.arrow-btn{position:absolute;width:40px;height:40px;border-radius:50%;background:#fff;border:1px solid #ddd;display:flex;align-items:center;justify-content:center;font-size:14px;color:#555}

/* features */
.features{top:2398px;height:589px;background:#fff}
.features h3{position:absolute;font:600 27px "Rajdhani",sans-serif;letter-spacing:.6px}
.features h4{position:absolute;font:500 17px "Raleway",sans-serif}

/* news */
.news{top:2987px;height:544px;background:var(--paler)}
.news .date{font-size:11px;margin-top:13px;color:#333}
.news h3{margin-top:8px}

/* banner */
.banner{top:3531px;height:202px;background:var(--orange);text-align:center;color:#fff}
.banner .kicker{position:absolute;top:42px;width:1200px;font-size:14px;color:#fff3e4}
.banner h2{position:absolute;top:60px;width:1200px;font:700 37px "Rajdhani",sans-serif;letter-spacing:.8px}
.banner .dl{position:absolute;left:529px;top:122px;width:137px;height:35px;background:var(--green);color:#fff;font-size:10.5px;font-weight:700;display:flex;align-items:center;justify-content:center}

/* about */
.about{top:3733px;height:462px}
.col{position:absolute;top:127px;width:300px}
.col h4{font:500 19px "Rajdhani",sans-serif;letter-spacing:.5px}
.col .rule{width:170px;height:1px;background:#ddd;margin:5px 0 10px}
.col p{font-size:12px;line-height:19px;color:var(--text)}
.divider{position:absolute;top:118px;width:1px;height:150px;background:#e2e2e2}
.partners-line{position:absolute;left:93px;top:338px;width:1014px;height:1px;background:#e6e6e6}
.partner{position:absolute;top:352px;width:150px;height:30px;background:#d5d5d5;border-radius:3px}

/* footer */
.site-footer{top:4195px;height:330px;background:var(--green-dark);color:#fff}
.f-col{position:absolute;top:50px}
.f-col h5{font:500 15px "Rajdhani",sans-serif;letter-spacing:.6px;margin-bottom:9px}
.f-col li{list-style:none;font-size:10.5px;color:#b9c2ae;line-height:27px}
.contact-line{display:flex;gap:6px;font-size:10.5px;color:#b9c2ae;line-height:14px;margin-bottom:24px}
.field{position:absolute;border:1px solid #4c5e3b;font-size:10px;color:#b9c2ae;padding:8px}
.send{position:absolute;left:1028px;top:197px;width:79px;height:28px;background:var(--orange);font-size:10px;display:flex;align-items:center;justify-content:center}
.social{position:absolute;left:586px;top:242px;width:28px;height:28px;border-radius:50%;border:2px solid #fff}
.copyright{position:absolute;top:280px;width:1200px;text-align:center;font-size:10px;color:#b9c2ae}
.copyright b{color:var(--orange);font-weight:600}
</style>
</head>
<body>

<header class="site-header">
  <div class="abs logo"><div class="logo-mark"></div><div class="logo-name">PELLMAR DRONES</div></div>
  <div class="abs topbar">
    <span><svg width="10" height="10" viewBox="0 0 10 10"><path d="M2 1l2 2-1 1.3a5 5 0 0 0 2.7 2.7L7 6l2 2-1.2 1.2C4.5 9 1 5.5.8 2.2z" fill="#fff"/></svg>+31 6 55501234</span>
    <span><svg width="11" height="8" viewBox="0 0 11 8"><rect width="11" height="8" fill="#fff"/><path d="M0 0l5.5 4.5L11 0" stroke="#f78f20" fill="none"/></svg>info@pellmardrones-example.com</span>
    <span>En ˅</span>
  </div>
  <nav class="nav">
    <a class="active" style="left:491px">HOME</a>
    <a style="left:566px">CROP MONITORING</a>
    <a style="left:710px">TECHNOLOGY</a>
    <a style="left:827px">ABOUT</a>
    <a style="left:907px">NEWS&amp;DOWNLOADS</a>
    <a style="left:1057px">CONTACT</a>
  </nav>
</header>

<section class="hero">
  <div class="photo hero-photo" role="img" aria-label="Orange drone flying over a greenhouse full of flowering crops"></div>
  <div class="abs hero-copy">
    <div class="kicker">PELLMAR DRONES</div>
    <h1>ENABLES AERIAL DATA<br>COLLECTION</h1>
  </div>
  <svg class="abs" style="left:0;top:490px" width="360" height="35" viewBox="0 0 360 35">
    <polygon points="0,35 0,0 357,0 322,35" fill="#fff"/>
    <path d="M250 17h24M250 17l5-4M250 17l5 4M283 17h24M307 17l-5-4M307 17l-5 4" stroke="#222" stroke-width="1.5" fill="none"/>
  </svg>
</section>

<section class="welcome">
  <div class="abs kicker">WELCOME TO</div>
  <h2>PELLMAR DRONES</h2>
  <p class="body-text">Pellmar Drones has developed a unique autonomous drone system that is able to fly and navigate in a greenhouse without manual interference. Based on a flight plan the drone follows the right coordinates in the greenhouse, day or night, collecting high accurate data. Data is being interpreted by Artificial Intelligence software resulting in crop improvement information. The focus is the following four customer pains: Development, Plant stress, Growth and Diseases.</p>
  <div class="btn" style="left:93px;top:367px;width:103px;height:36px">Read more</div>
  <div class="photo welcome-photo" role="img" aria-label="Orange drone hovering above farmland with a lake"></div>
</section>

<section class="applications">
  <div class="kicker">CROP MONITORING</div>
  <div class="title" style="top:62px">APPLICATIONS</div>
  <div class="app" style="left:120px"><div class="app-icon"><svg width="44" height="44" viewBox="0 0 44 44" fill="none" stroke="#fff" stroke-width="2.5"><path d="M22 30V16M22 22c-6 0-9-4-9-9 6 0 9 3 9 9zM22 18c0-5 3-8 9-8 0 5-3 8-9 8zM8 32h28"/></svg></div><div class="app-label">GROWTH</div></div>
  <div class="app" style="left:374px"><div class="app-icon"><svg width="44" height="44" viewBox="0 0 44 44" fill="none" stroke="#fff" stroke-width="2.5"><circle cx="22" cy="18" r="10"/><path d="M15 26v10M29 26v10"/></svg></div><div class="app-label">STRESS</div></div>
  <div class="app" style="left:626px"><div class="app-icon"><svg width="44" height="44" viewBox="0 0 44 44" fill="none" stroke="#fff" stroke-width="2.5"><path d="M22 6l13 5v10c0 9-6 14-13 17C15 35 9 30 9 21V11z"/><path d="M22 28v-8M22 22c-4 0-6-2-6-5 4 0 6 2 6 5zM22 20c0-3 2-5 6-5 0 3-2 5-6 5z"/></svg></div><div class="app-label">DEVELOPMENT</div></div>
  <div class="app" style="left:880px"><div class="app-icon"><svg width="44" height="44" viewBox="0 0 44 44" fill="#fff"><circle cx="22" cy="22" r="9"/><g stroke="#fff" stroke-width="2.5"><path d="M22 6v6M22 32v6M6 22h6M32 22h6M11 11l4 4M29 29l4 4M33 11l-4 4M15 29l-4 4"/></g><circle cx="19" cy="20" r="2" fill="#f78f20"/><circle cx="25" cy="25" r="1.5" fill="#f78f20"/></svg></div><div class="app-label">DISEASES</div></div>
</section>

<section class="tech">
  <div class="title" style="top:55px">TECHNOLOGY</div>
  <div class="card" style="left:93px;top:116px">
    <div class="photo" role="img" aria-label="Hands holding a tablet controlling a drone in a field" style="background:linear-gradient(160deg,#a8c48a,#3f6b2c 60%,#2d3f2a)"></div>
    <h3>Aerial Data Collection</h3>
    <p class="body-text">Sed ut perspiciatis unde omnis iste natus error sit voluptatem accusantium doloremque laudantium totam rem</p>
    <div class="btn" style="left:0;top:311px;width:95px;height:32px">Read more</div>
  </div>
  <div class="card" style="left:437px;top:116px">
    <div class="photo" role="img" aria-label="Aerial view of crop fields with a tree line" style="background:linear-gradient(150deg,#c9a25f,#8a7a3a 50%,#5c7232)"></div>
    <h3>Artificial intelligence</h3>
    <p class="body-text">Sed ut perspiciatis unde omnis iste natus error sit voluptatem accusantium doloremque laudantium totam rem</p>
    <div class="btn" style="left:0;top:311px;width:95px;height:32px">Read more</div>
  </div>
  <div class="card" style="left:781px;top:116px">
    <div class="photo" role="img" aria-label="Wide landscape of farmland under a cloudy sky" style="background:linear-gradient(180deg,#9aa6b8,#c6c6c0 45%,#5e7a3c 60%,#3c5428)"></div>
    <h3>Free Data Sets</h3>
    <p class="body-text">Sed ut perspiciatis unde omnis iste natus error sit voluptatem accusantium doloremque laudantium totam rem</p>
    <div class="btn" style="left:0;top:311px;width:95px;height:32px">Read more</div>
  </div>

  <div class="title" style="top:515px">MEET OUR TEAM</div>
  <div class="arrow-btn" style="left:27px;top:690px">‹</div>
  <div class="arrow-btn" style="left:1133px;top:690px">›</div>
  <div class="member" style="left:93px"><div class="photo" role="img" aria-label="Portrait of team member Aron Velde" style="background:linear-gradient(180deg,#c7c0ae,#8a6a45)"></div><h4>MR. ARON VELDE</h4><span>Farmer</span></div>
  <div class="member" style="left:351px"><div class="photo" role="img" aria-label="Portrait of team member Bram Hollis" style="background:linear-gradient(180deg,#d9dcde,#5a5a5a)"></div><h4>MR. BRAM HOLLIS</h4><span>Consultant</span></div>
  <div class="member" style="left:610px"><div class="photo" role="img" aria-label="Portrait of team member Tomas Riven" style="background:linear-gradient(180deg,#d4d4d2,#3f5f8a)"></div><h4>MR. TOMAS RIVEN</h4><span>Farmer</span></div>
  <div class="member" style="left:868px"><div class="photo" role="img" aria-label="Portrait of team member Lars Dekkar" style="background:linear-gradient(180deg,#9aa08e,#4a5a3e)"></div><h4>MR. LARS DEKKAR</h4><span>Farmer</span></div>
</section>

<section class="features">
  <div class="photo" role="img" aria-label="Drone silhouetted against a sunset over fields" style="left:93px;top:48px;width:492px;height:305px;background:linear-gradient(180deg,#e9ecec 0%,#f0d9b8 50%,#e0a55a 70%,#7c6a45 85%,#5a5a3c 100%)"></div>
  <div class="photo" role="img" aria-label="Orange drone flying inside a large greenhouse" style="left:619px;top:48px;width:488px;height:305px;background:linear-gradient(180deg,#8a8f8c,#b9bcb6 35%,#5f7f3c 70%,#3f5a2c)"></div>
  <svg class="abs" style="left:822px;top:176px" width="46" height="46" viewBox="0 0 46 46"><circle cx="23" cy="23" r="21" fill="rgba(255,255,255,.25)" stroke="#fff" stroke-width="2"/><polygon points="19,15 31,23 19,31" fill="#fff"/></svg>
  <h3 style="left:93px;top:367px">GREENHOUSE DRONE</h3>
  <h4 style="left:93px;top:405px">Crop monitoring by aerial data-collection</h4>
  <p class="abs body-text" style="left:93px;top:438px;width:490px">Using drones in greenhouses opens up opportunities to optimize the growth process. With the Pellmar drone a wide variety of data can be collected, which is analyzed using advanced Artificial Intelligence algorithms.</p>
  <div class="btn" style="left:93px;top:512px;width:95px;height:32px">Read more</div>
  <h3 style="left:619px;top:367px">SEED GERMINATION RATIO</h3>
  <p class="abs body-text" style="left:619px;top:405px;width:488px">Pellmar Drones is specialist in aerial data-collection and crop monitoring in horticulture. The drone flies autonomous in greenhouses, collects crop data and artificial intelligence software interpreted the data.</p>
  <div class="btn" style="left:619px;top:485px;width:95px;height:32px">Read more</div>
</section>

<section class="news">
  <div class="title" style="top:42px">RECENT NEWS</div>
  <div class="arrow-btn" style="left:27px;top:193px">‹</div>
  <div class="arrow-btn" style="left:1133px;top:193px">›</div>
  <div class="card" style="left:93px;top:114px">
    <div class="photo" role="img" aria-label="Drone over a golden field at sunset" style="background:linear-gradient(180deg,#c9c2b2,#e4a04a 55%,#7a4a1a)"></div>
    <div class="date">15 July, 2020</div><h3>Duis aute irure dolor in Reprehenderit</h3>
    <p class="body-text">Sed ut perspiciatis unde omnis iste natus error sit voluptatem accusantium doloremque laudantium totam rem</p>
    <div class="btn" style="left:0;top:334px;width:95px;height:32px">Read more</div>
  </div>
  <div class="card" style="left:437px;top:114px">
    <div class="photo" role="img" aria-label="Drone spraying a green rice paddy" style="background:linear-gradient(180deg,#e4ece6,#5f8f3a 40%,#8bbf4a)"></div>
    <div class="date">15 July, 2020</div><h3>Duis aute irure dolor in Reprehenderit</h3>
    <p class="body-text">Sed ut perspiciatis unde omnis iste natus error sit voluptatem accusantium doloremque laudantium totam rem</p>
    <div class="btn" style="left:0;top:334px;width:95px;height:32px">Read more</div>
  </div>
  <div class="card" style="left:781px;top:114px">
    <div class="photo" role="img" aria-label="Aerial view of a road crossing yellow and green fields" style="background:linear-gradient(160deg,#d6c23a,#6f8a3a 50%,#3f5a2c)"></div>
    <div class="date">15 July, 2020</div><h3>Duis aute irure dolor in Reprehenderit</h3>
    <p class="body-text">Sed ut perspiciatis unde omnis iste natus error sit voluptatem accusantium doloremque laudantium totam rem</p>
    <div class="btn" style="left:0;top:334px;width:95px;height:32px">Read more</div>
  </div>
</section>

<section class="banner">
  <div class="kicker">FINIBUS BONORUM</div>
  <h2>NOR AGAIN IS THERE ANYONE WHO LOVES OR PURSUES</h2>
  <div class="dl">DOWNLOAD NOW</div>
</section>

<section class="about">
  <div class="title" style="top:50px">ABOUT US</div>
  <div class="col" style="left:93px"><h4>OUR VISION</h4><div class="rule"></div><p>Our current and successful application is germination counting. Thousands of seedling trays are monitored within the shortest possible time. The result is an exact insight of the seedling rate and crop development status.</p></div>
  <div class="divider" style="left:430px"></div>
  <div class="col" style="left:453px"><h4>COMPANY</h4><div class="rule"></div><p>Our current and successful application is germination counting. Thousands of seedling trays are monitored within the shortest possible time. The result is an exact insight of the seedling rate and crop development status.</p></div>
  <div class="divider" style="left:773px"></div>
  <div class="col" style="left:812px"><h4>TESTIMONIALS</h4><div class="rule"></div><p>Sed ut perspiciatis unde omnis iste natus error sit voluptatem accusantium doloremque laudantium, totam rem aperiam, eaque ipsa quae ab illo inventore...</p><p style="color:#222;font-weight:600;margin-top:6px">Mr. Aron Velde</p></div>
  <div class="partners-line"></div>
  <div class="partner" style="left:93px;width:180px"></div>
  <div class="partner" style="left:355px;width:140px"></div>
  <div class="partner" style="left:595px;width:100px"></div>
  <div class="partner" style="left:805px;width:100px"></div>
  <div class="partner" style="left:1013px;width:94px"></div>
</section>

<footer class="site-footer">
  <div class="f-col" style="left:93px"><h5>QUICK LINKS</h5><ul><li>Home</li><li>Crop Monitoring</li><li>Technology</li><li>About Us</li><li>News &amp; Downloads</li><li>Contact Us</li></ul></div>
  <div class="f-col" style="left:300px"><h5>MARKETS</h5><ul><li>Breeding</li><li>Young plant</li><li>Potplants</li><li>Cutflowers</li><li>Vegetables</li><li>Soft fruit</li></ul></div>
  <div class="f-col" style="left:474px"><h5>CONTACTS</h5>
    <div class="contact-line" style="margin-top:14px"><svg width="9" height="12" viewBox="0 0 9 12"><path d="M4.5 0A4.5 4.5 0 0 0 0 4.5C0 8 4.5 12 4.5 12S9 8 9 4.5A4.5 4.5 0 0 0 4.5 0z" fill="#f78f20"/><circle cx="4.5" cy="4.5" r="1.6" fill="#1b3009"/></svg><span>Akkerlaan 12C,<br>6701XZ, Wenstad</span></div>
    <div class="contact-line"><svg width="10" height="10" viewBox="0 0 10 10"><path d="M2 1l2 2-1 1.3a5 5 0 0 0 2.7 2.7L7 6l2 2-1.2 1.2C4.5 9 1 5.5.8 2.2z" fill="#f78f20"/></svg><span>+31 6 55501234</span></div>
    <div class="contact-line"><svg width="11" height="8" viewBox="0 0 11 8"><rect width="11" height="8" fill="#f78f20"/><path d="M0 0l5.5 4.5L11 0" stroke="#1b3009" fill="none"/></svg><span>info@pellmardrones-example.com</span></div>
  </div>
  <div class="f-col" style="left:720px"><h5>SEND A MESSAGE</h5></div>
  <div class="field" style="left:720px;top:78px;width:190px;height:32px">Name:</div>
  <div class="field" style="left:720px;top:116px;width:190px;height:32px">Email:</div>
  <div class="field" style="left:720px;top:155px;width:190px;height:32px">Phone:</div>
  <div class="field" style="left:919px;top:78px;width:188px;height:109px">Message:</div>
  <div class="send">SEND</div>
  <div class="social"></div>
  <div class="copyright">COPYRIGHT © 2020 <b>PELLMAR DRONES</b>. ALL RIGHTS RESERVED.</div>
</footer>

</body>
</html>
```